Digital Album Cover - Frosted Lanterns (Night Falls Still)

HiI need a digital album cover for a piano instrumental cover single

Artist: Corey Dalton
Title: Frosted Lanterns (Night Falls Still)

The song was originally by Derek Holloway

Please use my logo

You can listen to the track herehttps://soundcloud.com/coreydaltonkeys/frosted-lanterns-night-falls-still-piano-instrumental-cover

Requirements
Must have
• My logo design Corey Dalton

```html
<!DOCTYPE html>
<html lang="en">
<head>
<meta charset="utf-8">
<title>Frosted Lanterns (Night Falls Still) – Corey Dalton</title>
<link rel="stylesheet" href="https://fonts.googleapis.com/css2?family=Cormorant+Garamond:wght@500;600&display=swap">
<style>
  :root {
    --title-white: #ece6ea;
    --artist-gold: #e2c35a;
    --logo-white: #ffffff;
    --pine-deep: #0d1408;
    --pine: #2a3812;
    --bauble-red: #7a1a10;
    --warm-gold: #8a6a22;
    --night: #0a0604;
  }
  html, body {
    margin: 0;
    padding: 0;
    width: 1200px;
    height: 1200px;
    overflow: hidden;
    background: var(--night);
  }
  .album-cover {
    position: relative;
    width: 1200px;
    height: 1200px;
    overflow: hidden;
  }
  .cover-photo {
    position: absolute;
    inset: 0;
    background:
      radial-gradient(ellipse 380px 300px at 220px 260px, rgba(170,120,40,0.55), transparent 70%),
      radial-gradient(ellipse 300px 260px at 700px 420px, rgba(130,30,20,0.6), transparent 70%),
      radial-gradient(ellipse 320px 360px at 1080px 480px, rgba(140,30,20,0.55), transparent 70%),
      radial-gradient(ellipse 360px 300px at 380px 720px, rgba(120,90,40,0.5), transparent 70%),
      linear-gradient(160deg, var(--warm-gold) 0%, var(--pine) 30%, var(--bauble-red) 55%, var(--pine-deep) 80%, var(--night) 100%);
  }
  .text-shade {
    position: absolute;
    left: 0; right: 0; bottom: 0;
    height: 340px;
    background: linear-gradient(to bottom, rgba(10,6,4,0), rgba(10,6,4,0.6));
  }
  .brand {
    position: absolute;
    left: 674px;
    top: 50px;
    height: 116px;
    display: flex;
    align-items: center;
    gap: 18px;
  }
  .brand-mark {
    width: 116px;
    height: 116px;
    border-radius: 50%;
    background: var(--logo-white);
    flex: none;
  }
  .brand-name {
    font-family: "Cormorant Garamond", serif;
    font-weight: 600;
    font-size: 46px;
    line-height: 1;
    color: var(--logo-white);
    white-space: nowrap;
  }
  .release-title {
    position: absolute;
    left: 72px;
    top: 982px;
    margin: 0;
    font-family: "Cormorant Garamond", serif;
    font-weight: 600;
    font-size: 60px;
    line-height: 1;
    color: var(--title-white);
    white-space: nowrap;
    text-transform: uppercase;
  }
  .release-title .subtitle {
    font-size: 50px;
  }
  .release-artist {
    position: absolute;
    left: 74px;
    top: 1064px;
    margin: 0;
    font-family: "Cormorant Garamond", serif;
    font-weight: 500;
    font-size: 60px;
    line-height: 1;
    color: var(--artist-gold);
    font-variant: small-caps;
    letter-spacing: 4px;
    white-space: nowrap;
  }
</style>
</head>
<body>
  <main class="album-cover">
    <div class="cover-photo" role="img" aria-label="Photograph of a grand piano with open sheet music in front of a lit Christmas tree with red baubles and gold ribbon"></div>
    <div class="text-shade"></div>

    <div class="brand">
      <div class="brand-mark"></div>
      <span class="brand-name">COREY DALTON</span>
    </div>

    <h1 class="release-title">Frosted Lanterns <span class="subtitle">(Night Falls Still)</span></h1>
    <p class="release-artist">Corey Dalton</p>
  </main>
</body>
</html>
```